Web Design Project

Please take a look at my current aged website www.tarlowpeopleadvisory.com and my newly designed logo and business cards. I would like a new fresh updated look to my website and my new designs incorporated.
Updates

  Good Morning Everyone

Due to an Austrralian licencing issue I have had to have my logo slightly redesigned.

Would you please be able to look at the newly uploaded files and revise your designs.

Thanks so much.  I am very happy with the calibre and quality of the designs so far.

kind Regards

Marnie

Industry/Entity Type

Business

Requirements
Must have
• the exisiting pages and fresh new graphics and a real commitment to my palette of lime green, turqouise and black.

```html
<!DOCTYPE html>
<html lang="en">
<head>
<meta charset="utf-8">
<title>Tarlow Consulting – Outsourced Human Resources</title>
<link rel="stylesheet" href="https://fonts.googleapis.com/css2?family=Ubuntu:wght@400;500&family=Comfortaa:wght@400&family=Arimo:wght@400&family=PT+Sans:ital,wght@0,400;1,400&family=Michroma&family=Oswald:wght@400&display=swap">
<style>
:root{
  --lime:#57c22b;
  --turq:#1a9ad6;
  --sky:#5aa4d6;
  --ink:#111;
  --text:#6a6a6a;
  --page:#ececec;
  --panel:#f6f6f6;
  --white:#fff;
  --rule:#dedede;
}
*{margin:0;padding:0;box-sizing:border-box}
html,body{width:733px;height:1200px;overflow:hidden}
body{position:relative;background:var(--page);font-family:"PT Sans",sans-serif;color:var(--text)}
.abs{position:absolute}

.site-header{left:0;top:0;width:733px;height:108px;background:var(--white);border-bottom:1px solid var(--rule)}
.brand{left:44px;top:12px;width:150px;height:72px;display:flex;flex-direction:column;align-items:center;justify-content:center;gap:4px}
.brand-dot{width:30px;height:30px;border-radius:50%;background:var(--turq)}
.brand-name{font-family:"Ubuntu",sans-serif;font-size:16px;color:var(--turq);white-space:nowrap}
.tagline{left:192px;top:0;width:338px;height:80px;background:#f7f7f7;box-shadow:0 3px 6px rgba(0,0,0,.25);border:1px solid #e2e2e2;font-family:"Comfortaa",sans-serif;font-size:18.5px;line-height:27px;white-space:nowrap}
.tagline .l1{position:absolute;left:18px;top:9px;color:#5ab8df}
.tagline .l2{position:absolute;right:16px;top:36px;color:var(--lime)}
.social{left:553px;top:27px;display:flex;align-items:center;gap:2px;font-family:"Arimo",sans-serif;font-size:9px;color:#333}
.social span{margin-right:3px}
.social i{display:block;width:19px;height:19px;border-radius:3px;background:var(--sky)}
.search{left:553px;top:56px;width:142px;height:17px;background:#e9e9e9;border:1px solid #ddd}
.search svg{position:absolute;right:5px;top:4px}

.main-nav{left:43px;top:129px;width:652px;height:39px;background:var(--white);box-shadow:0 1px 3px rgba(0,0,0,.12);font-family:"Ubuntu",sans-serif;font-size:9.5px}
.main-nav a{position:absolute;top:0;line-height:39px;color:var(--turq);text-decoration:none;white-space:nowrap}
.main-nav a.active{left:0;top:-5px;width:62px;height:44px;line-height:54px;background:var(--lime);color:var(--white);text-align:center}

.hero{left:43px;top:190px;width:652px;height:286px;background:linear-gradient(90deg,#e6e6e6,#fafafa 60%,#fff);box-shadow:0 4px 6px rgba(0,0,0,.25)}
.hero-figure{left:10px;top:90px;width:340px;height:196px;background:linear-gradient(90deg,#d8d8d8,#9a9a9a 55%,#2a2a2a 75%,#efefef)}
.hero-title{left:25px;top:10px;font-family:"Arimo",sans-serif;font-weight:400;font-size:31px;line-height:31px;letter-spacing:.6px;color:var(--ink);white-space:nowrap}
.hero-steps{left:478px;top:93px;font-family:"Arimo",sans-serif;font-size:29px;line-height:31px;color:var(--turq);list-style:none;white-space:nowrap}

.bar{background:var(--lime);color:var(--white);font-family:"Ubuntu",sans-serif;font-weight:400;font-size:13.5px;height:47px;line-height:47px;padding-left:10px;white-space:nowrap}
.intro-bar{left:43px;top:497px;width:434px}
.services-bar{left:478px;top:497px;width:217px;font-weight:500}
.intro{left:43px;top:544px;width:434px;height:254px;background:var(--panel)}
.services{left:478px;top:544px;width:217px;height:254px;background:var(--panel);border-left:1px solid var(--rule)}
.intro-figure{left:18px;top:14px;width:56px;height:130px;background:radial-gradient(ellipse at 50% 30%,#fff,#cfcfcf 70%);border-radius:28px 28px 10px 10px}
.intro p{position:absolute;font-size:7.6px;line-height:13.3px}
.services ul{list-style:none;position:absolute;left:18px;top:11px}
.services li{height:23.4px;font-size:10px;color:#777;display:flex;align-items:center;gap:8px;white-space:nowrap}
.services li svg{flex:none}

.feature{top:813px;width:201px}
.feature-img{width:201px;height:123px;background:linear-gradient(180deg,#0c1e5c,#2b4d8f 55%,#a0a090 70%,#3a3a3a)}
.feature h3{font-family:"Michroma",sans-serif;font-weight:400;font-size:10px;line-height:17px;color:var(--turq);margin-top:9px;white-space:nowrap}
.feature .lead{font-style:italic;font-size:10px;line-height:14px;color:#444;margin-top:2px}
.feature .body{font-size:7.8px;line-height:13.5px;margin-top:14px}
.more{display:block;width:45px;height:25px;line-height:25px;text-align:center;background:var(--sky);color:var(--white);font-family:"Ubuntu",sans-serif;font-size:11px;text-decoration:none}

.chat{left:499px;top:813px;width:196px;height:71px;background:var(--sky);color:var(--white);font-family:"Oswald",sans-serif;white-space:nowrap}
.chat .big{position:absolute;left:15px;top:2px;font-size:22px}
.chat .big small{font-size:13px}
.chat .sub{position:absolute;right:10px;top:23px;font-size:14px}
.chat .btn{position:absolute;left:15px;top:49px;width:58px;height:17px;background:var(--white);color:var(--sky);font-family:"PT Sans",sans-serif;font-size:7px;line-height:17px;text-align:center}
.news-bar{left:478px;top:888px;width:217px;font-weight:500}
.email{left:490px;top:952px;width:186px;height:28px;background:#e4e4e4;border:1px solid #d6d6d6;font-size:8px;line-height:28px;padding-left:9px;color:#888}
.subscribe{left:597px;top:992px;width:78px;height:29px;background:var(--sky);color:var(--white);font-family:"Ubuntu",sans-serif;font-size:12.5px;line-height:29px;text-align:center}

.site-footer{left:0;top:1116px;width:733px;height:84px;background:var(--white);border-top:1px solid var(--rule)}
.footer-brand{left:44px;top:8px;width:120px;height:64px;display:flex;flex-direction:column;align-items:center;justify-content:center;gap:4px}
.footer-brand .brand-dot{width:26px;height:26px;background:#666}
.footer-brand .brand-name{font-size:14px;color:#555}
.footer-nav{right:35px;top:35px;font-size:9px;color:#333;word-spacing:1px;white-space:nowrap}
.footer-nav b{font-weight:400;margin:0 18px;color:#333}
.copyright{right:39px;top:61px;font-size:7px;color:#888;white-space:nowrap}
</style>
</head>
<body>

<header class="site-header abs">
  <div class="brand abs"><i class="brand-dot"></i><span class="brand-name">Tarlow Consulting</span></div>
  <div class="tagline abs"><span class="l1">Outsourced Human Resources</span><span class="l2">Solutions &amp; Strategies</span></div>
  <div class="social abs"><span>SOCIALIZE WITH US</span><i></i><i></i><i></i></div>
  <div class="search abs"><svg width="8" height="8" viewBox="0 0 8 8"><circle cx="3" cy="3" r="2.2" fill="none" stroke="#888" stroke-width="1"/><line x1="4.6" y1="4.6" x2="7.5" y2="7.5" stroke="#888"/></svg></div>
</header>

<nav class="main-nav abs">
  <a class="active" href="#">HOME</a>
  <a href="#" style="left:78px">OUR SERVICES</a>
  <a href="#" style="left:173px">OUR CONSULTANTS</a>
  <a href="#" style="left:280px">OUR FEES</a>
  <a href="#" style="left:353px">CONTACT US</a>
</nav>

<section class="hero abs">
  <div class="hero-figure abs" role="img" aria-label="Faded silhouette of a thinking person repeated in layers"></div>
  <h1 class="hero-title abs">The Box Wasn't Designed For Thinking<br>You were...</h1>
  <ol class="hero-steps abs"><li>1. Think</li><li>2. Analyze</li><li>3. Present</li></ol>
</section>

<h2 class="bar intro-bar abs">WHAT CAN TARLOW HR CONSULTING DO FOR ME?</h2>
<h2 class="bar services-bar abs">MAIN SERVICES</h2>

<section class="intro abs">
  <div class="intro-figure abs" role="img" aria-label="3D white figure standing with arms crossed"></div>
  <p style="left:93px;top:17px;width:322px">During these challenging economic times it can be difficult to justify internal human resources management services or support. However as a business owner or Manager you may find that HR support or advice is required from time to time.</p>
  <p style="left:93px;top:73px;width:322px">&nbsp;Tarlow HR Consulting are an outsourced HR function. &nbsp;We can provide you with that ongoing support, offer solutions and assist you with developing strategies that fit your business and deliver results.<br>During these challenging economic times it can be difficult to justify internal human resources management services or support. However as a business owner or Manager you may find that HR support or advice is required from time to time.</p>
  <p style="left:15px;top:183px;width:410px">During these challenging economic times it can be difficult to justify internal human resources management services or support. However as a business owner or Manager you may find that HR support or advice is required from time to time.</p>
</section>

<aside class="services abs">
  <ul>
    <li><svg width="11" height="11" viewBox="0 0 12 12"><path d="M6 0l1.4 2.6L10.2 1.8 9.4 4.6 12 6 9.4 7.4l.8 2.8-2.8-.8L6 12 4.6 9.4l-2.8.8.8-2.8L0 6l2.6-1.4-.8-2.8 2.8.8z" fill="#1a9ad6"/></svg>Architecture</li>
    <li><svg width="11" height="11" viewBox="0 0 12 12"><path d="M6 0l1.4 2.6L10.2 1.8 9.4 4.6 12 6 9.4 7.4l.8 2.8-2.8-.8L6 12 4.6 9.4l-2.8.8.8-2.8L0 6l2.6-1.4-.8-2.8 2.8.8z" fill="#1a9ad6"/></svg>Master Planning</li>
    <li><svg width="11" height="11" viewBox="0 0 12 12"><path d="M6 0l1.4 2.6L10.2 1.8 9.4 4.6 12 6 9.4 7.4l.8 2.8-2.8-.8L6 12 4.6 9.4l-2.8.8.8-2.8L0 6l2.6-1.4-.8-2.8 2.8.8z" fill="#1a9ad6"/></svg>Feasibility Studies</li>
    <li><svg width="11" height="11" viewBox="0 0 12 12"><path d="M6 0l1.4 2.6L10.2 1.8 9.4 4.6 12 6 9.4 7.4l.8 2.8-2.8-.8L6 12 4.6 9.4l-2.8.8.8-2.8L0 6l2.6-1.4-.8-2.8 2.8.8z" fill="#1a9ad6"/></svg>Site Analysis &amp; Selection</li>
    <li><svg width="11" height="11" viewBox="0 0 12 12"><path d="M6 0l1.4 2.6L10.2 1.8 9.4 4.6 12 6 9.4 7.4l.8 2.8-2.8-.8L6 12 4.6 9.4l-2.8.8.8-2.8L0 6l2.6-1.4-.8-2.8 2.8.8z" fill="#1a9ad6"/></svg>Needs Analysis</li>
    <li><svg width="11" height="11" viewBox="0 0 12 12"><path d="M6 0l1.4 2.6L10.2 1.8 9.4 4.6 12 6 9.4 7.4l.8 2.8-2.8-.8L6 12 4.6 9.4l-2.8.8.8-2.8L0 6l2.6-1.4-.8-2.8 2.8.8z" fill="#1a9ad6"/></svg>3D Modeling / Rendering</li>
    <li><svg width="11" height="11" viewBox="0 0 12 12"><path d="M6 0l1.4 2.6L10.2 1.8 9.4 4.6 12 6 9.4 7.4l.8 2.8-2.8-.8L6 12 4.6 9.4l-2.8.8.8-2.8L0 6l2.6-1.4-.8-2.8 2.8.8z" fill="#1a9ad6"/></svg>Predesign</li>
    <li><svg width="11" height="11" viewBox="0 0 12 12"><path d="M6 0l1.4 2.6L10.2 1.8 9.4 4.6 12 6 9.4 7.4l.8 2.8-2.8-.8L6 12 4.6 9.4l-2.8.8.8-2.8L0 6l2.6-1.4-.8-2.8 2.8.8z" fill="#1a9ad6"/></svg>Schematic design</li>
    <li><svg width="11" height="11" viewBox="0 0 12 12"><path d="M6 0l1.4 2.6L10.2 1.8 9.4 4.6 12 6 9.4 7.4l.8 2.8-2.8-.8L6 12 4.6 9.4l-2.8.8.8-2.8L0 6l2.6-1.4-.8-2.8 2.8.8z" fill="#1a9ad6"/></svg>Design development</li>
    <li><svg width="11" height="11" viewBox="0 0 12 12"><path d="M6 0l1.4 2.6L10.2 1.8 9.4 4.6 12 6 9.4 7.4l.8 2.8-2.8-.8L6 12 4.6 9.4l-2.8.8.8-2.8L0 6l2.6-1.4-.8-2.8 2.8.8z" fill="#1a9ad6"/></svg>Construction documents</li>
  </ul>
</aside>

<article class="feature abs" style="left:43px">
  <div class="feature-img" role="img" aria-label="Curved modern bridge in front of a tower at dusk"></div>
  <h3>NEW PERSPECTIVES IN<br>ARCHITECTURAL DESIGN</h3>
  <p class="lead">Est omnis doloresereledusempquibdameto aurerumoms odes necessitatibus saepe eveniet redums.</p>
  <p class="body">Etoluptates estudesu usandaeltaque earumrerum hictenetura sapiravi. Reiciendis vptatibus ass maioresaliasumes.</p>
</article>
<a class="more abs" href="#" style="left:150px;top:1079px">more</a>

<article class="feature abs" style="left:274px">
  <div class="feature-img" role="img" aria-label="Curved modern bridge in front of a tower at dusk"></div>
  <h3>NEW PERSPECTIVES IN<br>ARCHITECTURAL DESIGN</h3>
  <p class="lead">Est omnis doloresereledusempquibdameto aurerumoms odes necessitatibus saepe eveniet redums.</p>
  <p class="body">Etoluptates estudesu usandaeltaque earumrerum hictenetura sapiravi. Reiciendis vptatibus ass maioresaliasumes.</p>
</article>
<a class="more abs" href="#" style="left:392px;top:1079px">more</a>

<div class="chat abs">
  <span class="big">24/7 <small>ONLINE</small></span>
  <span class="sub">SUPPORT CHAT</span>
  <span class="btn">CLICK HERE!</span>
</div>
<h2 class="bar news-bar abs">NEWSLETTER SIGNUP</h2>
<div class="email abs">Your email address</div>
<div class="subscribe abs">Subscribe</div>

<footer class="site-footer abs">
  <div class="footer-brand abs"><i class="brand-dot"></i><span class="brand-name">Tarlow Consulting</span></div>
  <div class="footer-nav abs">Home<b>|</b>Our Services<b>|</b>Our Consultants<b>|</b>Our Fees<b>|</b>Contact Us</div>
  <div class="copyright abs">copyright@2012. All Rights Reserved</div>
</footer>

</body>
</html>
```